Dance School Banner Design

Design a banner with landscape orientation for outdoor use and advertisement for Dance School.

Tha dance school is Marlow Street Dance Academy and they have their own logo (please message for the file to be sent to you) utilising lots of colour.

Their brand and uniform colours are purple and golden yellow.

Must have the name/logo.

Must attract all ages, boys and girls.

MSDA offers dance class for all ages and all levels of ability in the following dance styles:

Classical Ballet
Jazz
Tap
Modern / Contemporary
Hip Hop
Cheerleading
Fitzla (licensed logo is available please message for this)
Fitzlakids (licensed logo is available please message for this)
Boys Class
Adults Classes

They offer all classes for fun or for competition.

Offer exams in Classical Ballet, Jazz and Tap.

Target Market(s)

All ages

Industry/Entity Type

Landscape

Requirements
Must have
• What classes are offered

Logo - 2 designs uploaded must use Marlow Street Dance Academy one, may wish to include home of "FALCONS" logo aswell please message for this to be sent to you

Phone Number 0493 516 247

Email address street-steps@mailbox-example.net

website address marlowstreetdance-example.com (this website is not live yet please see preview by using this link http://preview.dev.kovasite-example.com/index.php?admin_action=preview_mod&site_id=5820461739&template_id=617&industry=kovacheersites-example.com)
Nice to have
• Images of dancers (can provide some if needed)
Should not have
• Anything vulgar or discriminatory

```html
<!DOCTYPE html>
<html lang="en">
<head>
<meta charset="utf-8">
<title>Marlow Street Dance Academy – Banner</title>
<link rel="stylesheet" href="https://fonts.googleapis.com/css2?family=Cabin+Condensed:wght@700&family=Questrial&display=swap">
<style>
  :root {
    --purple: #6b2a86;
    --purple-deep: #53196c;
    --gold: #c9a13a;
    --gold-light: #f1dc8f;
    --beige: #eadbc0;
    --white: #ffffff;
  }
  * { margin: 0; padding: 0; box-sizing: border-box; }
  html, body { width: 1200px; height: 601px; overflow: hidden; background: var(--white); }
  .banner {
    position: relative;
    width: 1200px;
    height: 601px;
    overflow: hidden;
    background: var(--white);
    font-family: "Questrial", sans-serif;
  }
  .gold-rule {
    position: absolute; left: 0; width: 1200px;
    background: linear-gradient(90deg, var(--gold), var(--gold-light) 50%, var(--gold));
  }
  .gold-rule--top { top: 0; height: 12px; }
  .gold-rule--strip-top { top: 253px; height: 9px; }
  .gold-rule--strip-bottom { top: 397px; height: 9px; }
  .silhouette {
    position: absolute;
    background: radial-gradient(ellipse at center, rgba(234,219,192,0.9), rgba(234,219,192,0) 70%);
  }
  .silhouette--left { left: 0; top: 12px; width: 320px; height: 241px; }
  .silhouette--right { left: 900px; top: 12px; width: 300px; height: 241px; }

  .tagline {
    position: absolute; left: 26px; top: 40px;
    font-family: "Cabin Condensed", sans-serif;
    font-weight: 700; font-size: 42px; line-height: 47px;
    color: var(--purple); letter-spacing: 0.5px;
  }
  .studio-name {
    position: absolute; left: 300px; top: 50px; width: 620px;
    text-align: center; color: var(--purple);
    font-family: "Questrial", sans-serif;
  }
  .studio-name__main { display: block; font-size: 72px; line-height: 84px; }
  .studio-name__sub { display: block; font-size: 44px; line-height: 52px; }

  .team-name {
    position: absolute; left: 965px; top: 60px; width: 210px;
    text-align: center; color: var(--purple);
    font-family: "Cabin Condensed", sans-serif; font-weight: 700;
  }
  .team-name__home { display: block; font-size: 28px; line-height: 32px; }
  .team-name__team { display: block; font-size: 46px; line-height: 52px; }

  .photo-strip {
    position: absolute; left: 0; top: 262px; width: 1200px; height: 135px;
    display: flex;
  }
  .photo { height: 100%; }
  .photo--troupe { width: 180px; background: linear-gradient(135deg, #e8792d, #a8442a 60%, #5a4a46); }
  .photo--jazz { width: 190px; background: linear-gradient(135deg, #6f6a66, #a7a19b 55%, #4d4845); }
  .photo--cheer { width: 210px; background: linear-gradient(135deg, #7d7a77, #e7d15b 50%, #59575a); }
  .photo--hiphop { width: 260px; background: linear-gradient(135deg, #5f8fb5, #b9d4e6 50%, #7aa3c6); }
  .photo--ballet { width: 360px; background: linear-gradient(135deg, #8d8783, #efc3d8 45%, #6d6764); }

  .classes-band { position: absolute; left: 0; top: 406px; width: 1200px; height: 150px; }
  .class-list {
    position: absolute; left: 0; top: 445px; width: 1200px;
    text-align: center; color: var(--white);
    font-size: 30px; line-height: 34px;
  }
  .class-list__line { display: block; }
  .class-list__line--first { padding-left: 110px; }
  .class-list__line--second { padding-left: 40px; }
  .class-list__line--third { padding-left: 40px; }
  .bullet { color: var(--gold-light); }
  .phone {
    position: absolute; left: 14px; top: 512px;
    color: var(--gold-light); font-size: 32px;
  }
  .info-bar {
    position: absolute; left: 0; top: 556px; width: 1200px; height: 40px;
    background: linear-gradient(90deg, var(--gold), var(--gold-light) 50%, var(--gold));
    color: var(--purple-deep);
    font-size: 22px; line-height: 40px; text-align: center;
  }
  .info-bar .bullet { color: var(--purple); }
</style>
</head>
<body>
<div class="banner">
  <div class="gold-rule gold-rule--top"></div>
  <div class="silhouette silhouette--left" role="img" aria-label="Faint beige dancer silhouette"></div>
  <div class="silhouette silhouette--right" role="img" aria-label="Faint beige cheerleader silhouette"></div>

  <p class="tagline">ALL AGES,<br>BOYS<br>AND GIRLS</p>

  <h1 class="studio-name">
    <span class="studio-name__main">Marlow Street</span>
    <span class="studio-name__sub">Dance Academy</span>
  </h1>

  <p class="team-name">
    <span class="team-name__home">HOME OF</span>
    <span class="team-name__team">FALCONS</span>
  </p>

  <div class="gold-rule gold-rule--strip-top"></div>
  <div class="photo-strip">
    <div class="photo photo--troupe" role="img" aria-label="Dance troupe in orange costumes"></div>
    <div class="photo photo--jazz" role="img" aria-label="Jazz dancer mid-leap"></div>
    <div class="photo photo--cheer" role="img" aria-label="Cheerleader doing the splits with gold pom-poms"></div>
    <div class="photo photo--hiphop" role="img" aria-label="Hip hop dancer in a floor freeze"></div>
    <div class="photo photo--ballet" role="img" aria-label="Young ballet class in pink tutus"></div>
  </div>
  <div class="gold-rule gold-rule--strip-bottom"></div>

  <svg class="classes-band" viewBox="0 0 1200 150" aria-hidden="true">
    <defs>
      <linearGradient id="band-gold" x1="0" x2="1">
        <stop offset="0" stop-color="#c9a13a"/>
        <stop offset="0.5" stop-color="#f1dc8f"/>
        <stop offset="1" stop-color="#c9a13a"/>
      </linearGradient>
    </defs>
    <path d="M0 30 C 60 20, 110 10, 170 18 C 400 10, 800 8, 1000 18 C 1080 20, 1140 28, 1200 34 L1200 150 L0 150 Z" fill="url(#band-gold)"/>
    <path d="M0 36 C 60 26, 110 16, 170 24 C 400 16, 800 14, 1000 24 C 1080 26, 1140 34, 1200 40 L1200 150 L0 150 Z" fill="#6b2a86"/>
  </svg>

  <p class="class-list">
    <span class="class-list__line class-list__line--first">Classical Ballet <span class="bullet">•</span>Jazz <span class="bullet">•</span> Tap <span class="bullet">•</span> Modern / Contemporary <span class="bullet">•</span> Hip Hop</span>
    <span class="class-list__line class-list__line--second"><span class="bullet">•</span> Cheerleading <span class="bullet">•</span> Fitzla <span class="bullet">•</span> Fitzlakids</span>
    <span class="class-list__line class-list__line--third"><span class="bullet">•</span>Boys Classes <span class="bullet">•</span>Adults Classes</span>
  </p>
  <p class="phone">Ph. 0493 516 247</p>

  <p class="info-bar">CLASSES FOR FUN OR FOR COMPETITION <span class="bullet">•</span> OFFER EXAMS IN CLASSICAL BALLET, JAZZ AND TAP.</p>
</div>
</body>
</html>
```